Creative, Modern and Conversion based Web Design

Kovel Digital has recently launched a new logo and as part of our companies rebranding, we need a new website aimed towards the UK B2B marketplace.

The website needs to deliver a modern and creative website design whilst ensuring the design is tailored towards conversion optimisation.

This site must drive point of contact either from an online form, via a direct telephone call or Skype connection.

Our sales are all offline so the website will be a simple, elegant and stunning information portal.

Kovel Digital offers Digital Marketing services to companies throughout the UK - our target audiences are companies that turnover a minimum of 3 million pounds a year and as such we need to deliver a professional image that installs confidence in our companies abilities.

We do not like websites that are reliant upon stock photography - we are happy for stock photography to be used in a small way however the site must not look like a template filled with stock photography.

What do we do

We supply digital marketing services to those companies who demand a strong return on investment - our company prides itself on delivering successful campaigns that help establish long-term profitable relationships.

A lot of the information presented on our old site is relevant today however the design sucks. So please use the information on our current website as a foundation for your design content.

I am looking for several page designs including

"Home Page" Desktop Version
"Service Page" Desktop Version
"Blog Page" Desktop Version

"Home Page" Mobile Version
"Service Page" Mobile Version
"Blog Page" Mobile Version

In the 1st instance please only submit a single design for the "Home Page" Desktop Version - those designers that we are impressed with will be asked to complete the other designs before a winner is selected.

I like modern clean fonts - the site needs to welcome the reader and encourage them to absorb the information - not to overload and make them leave.

The site must be designed to naturally fit our companies new logo.

NO TEMPLATES

Target Market(s)

B2b - 3 million turnover and above

Industry/Entity Type

Digital Marketing

Number of Pages Required

3 page

Requirements
Must have
• Blended well with the companies logo
• We need conversion optimisation to be a huge part of the design - we considered a conversation when a potential customer reaches out to use via - web form, telephone or skype
• The current content on the old website fits today's business but the design sucks.
• www.koveldigital-studio.net
Nice to have
• We need 3 pages (in 2 variants Desktop and Mobile)
• Home Page
• Service Page
• Blog Page
• Please only deliver the "Home Page" desktop version - if we are happy with your design we will aks for the additional pages
Should not have
• No templates and not stock photo heavy design

```html
<!DOCTYPE html>
<html lang="en">
<head>
<meta charset="utf-8">
<title>Kovel Digital – Search Marketing That Actually Delivers</title>
<link rel="stylesheet" href="https://fonts.googleapis.com/css2?family=Montserrat:wght@400;500;600;700;800&family=Open+Sans:wght@400;600;700&display=swap">
<style>
:root{
  --blue:#2a7fe6;
  --blue-deep:#1a5cc9;
  --navy:#173a78;
  --ink:#1d2b45;
  --text:#5b6473;
  --muted:#8b93a1;
  --line:#d7dde6;
  --pale:#f3f6fa;
  --white:#ffffff;
  --tile:#e7f0fc;
}
*{box-sizing:border-box;margin:0;padding:0}
html,body{width:1200px;height:5085px;overflow:hidden}
body{position:relative;background:var(--white);font-family:"Open Sans",Arial,sans-serif;color:var(--text)}
h1,h2,h3,h4,.brand,.stat-num,.btn{font-family:"Montserrat",Arial,sans-serif}
.abs{position:absolute}

/* hero */
.hero{position:absolute;left:0;top:0;width:1200px;height:480px;background:linear-gradient(135deg,var(--blue) 0%,var(--blue-deep) 100%);overflow:hidden}
.hero-wave{position:absolute;left:0;bottom:0;width:1200px;height:140px}
.brand{display:flex;align-items:center;gap:10px;font-weight:700;font-size:22px;letter-spacing:.5px}
.brand-mark{width:22px;height:22px}
.site-brand{left:60px;top:22px;color:var(--white)}
.site-brand .brand-mark{background:var(--white)}
.nav{right:70px;top:24px;display:flex;align-items:center;gap:28px;color:var(--white);font-size:14px;font-weight:600}
.nav-social{display:flex;gap:14px;margin-left:14px}
.dot{width:16px;height:16px;border-radius:50%;background:var(--white)}
.hero h1{left:70px;top:136px;width:560px;color:var(--white);font-size:40px;line-height:50px;font-weight:700}
.hero-lead{left:70px;top:262px;width:440px;color:#e6efff;font-size:17px;line-height:27px}
.btn{display:inline-flex;align-items:center;justify-content:center;background:var(--navy);color:var(--white);font-weight:700;font-size:14px;border-radius:3px}
.hero-btn{left:70px;top:334px;width:180px;height:48px}
.hero-art{left:760px;top:170px;width:360px;height:270px;border-radius:14px;background:linear-gradient(160deg,#f4f8ff 0%,#c8dcf6 100%)}

/* partners */
.partners{left:70px;top:520px;width:1060px;display:flex;justify-content:space-between}
.partner{width:120px;height:40px;border-radius:6px;background:#e3e7ed}

/* intro */
.intro{left:70px;top:612px;width:1060px;text-align:center}
.intro h2{color:var(--ink);font-size:27px;font-weight:700;margin-bottom:22px}
.intro p{font-size:14px;line-height:24px;margin-bottom:14px}
.intro a{color:var(--blue)}
.intro strong{color:var(--ink)}

/* services */
.service{width:330px;text-align:center}
.service-icon{width:64px;height:64px;margin:0 auto 18px;border:2px solid var(--navy);border-radius:6px;background:var(--tile)}
.service h3{color:var(--ink);font-size:17px;font-weight:700;margin-bottom:10px}
.service p{font-size:13.5px;line-height:22px;padding:0 20px}

/* growth */
.growth-band{left:0;top:1380px;width:1200px;height:520px}
.growth-art{left:460px;top:1260px;width:340px;height:300px;border-radius:10px;background:linear-gradient(170deg,#f2f5f9 0%,#d5deea 100%)}
.growth-title{left:0;top:1594px;width:1200px;text-align:center;color:var(--white);font-size:30px;line-height:42px;font-weight:700}
.stat{width:300px;text-align:center}
.stat-num{color:var(--navy);font-size:46px;font-weight:800;line-height:56px}
.stat-label{color:var(--white);font-size:16px;font-weight:700;font-family:"Montserrat",Arial,sans-serif}

/* handle seo */
.seo{left:70px;top:1970px;width:600px}
.seo h2{color:var(--ink);font-size:25px;font-weight:700;margin-bottom:8px}
.seo h4{color:var(--ink);font-size:16px;font-weight:600;margin-bottom:16px}
.seo p{font-size:14px;line-height:24px}
.seo a{color:var(--blue)}
.seo-art{left:800px;top:1880px;width:290px;height:280px;border-radius:10px;background:linear-gradient(160deg,#eef4fd 0%,#c9daf3 100%)}

/* process */
.process-art{left:100px;top:2300px;width:310px;height:360px;border-radius:10px;background:linear-gradient(160deg,#eef4fd 0%,#cddcf1 100%)}
.process{left:480px;top:2232px;width:650px}
.process h2{color:var(--ink);font-size:27px;line-height:36px;font-weight:700;margin-bottom:26px}
.process ol{list-style:none}
.process li{font-size:14px;line-height:23px;margin-bottom:24px}
.process li b{color:var(--ink)}
.process .more{font-size:14px;font-weight:600;color:var(--ink)}
.process .more a{color:var(--blue);font-weight:400}

/* contact */
.contact-bg{left:0;top:2920px;width:1200px;height:1480px;background:var(--pale)}
.contact-band{left:0;top:2920px;width:1200px;height:420px;background:linear-gradient(135deg,var(--blue) 0%,var(--blue-deep) 100%)}
.contact-head{left:0;top:2990px;width:1200px;text-align:center;color:var(--white)}
.contact-head h2{font-size:28px;font-weight:700;margin-bottom:14px}
.contact-head p{font-size:14px;line-height:22px;color:#e3edff}
.card{left:70px;top:3150px;width:1060px;height:960px;background:var(--white);border-radius:4px;box-shadow:0 10px 40px rgba(23,58,120,.12)}
.card h3{color:var(--ink);font-size:17px;font-weight:700}
.form{left:30px;top:40px;width:420px}
.field{position:absolute;left:0;width:280px}
.field label{display:block;font-size:13.5px;margin-bottom:10px}
.input{height:38px;border:1px solid var(--line);border-radius:2px}
.textarea{height:150px}
.form-btn{position:absolute;left:0;top:820px;width:170px;height:46px}
.details{left:590px;top:40px;width:300px}
.detail{position:absolute;left:0;display:flex;gap:14px;font-size:13.5px;line-height:22px}
.detail svg{flex:none;margin-top:3px}
.detail-text{position:absolute;left:0;width:280px;font-size:13.5px;line-height:22px}
.follow{position:absolute;left:0;top:480px}
.follow-dots{display:flex;gap:14px;margin-top:14px}
.follow-dots .dot{background:var(--blue)}

/* footer */
.footer-brand{left:70px;top:4470px;color:var(--navy)}
.footer-brand .brand-mark{background:var(--navy)}
.footer-col{top:4468px;width:230px}
.footer-col h4{color:var(--ink);font-size:15px;font-weight:700;margin-bottom:18px}
.footer-col li{list-style:none;font-size:13px;line-height:30px;color:var(--muted)}
.footer-rule{left:0;top:4980px;width:1200px;height:1px;background:#e9edf2}
.copyright{left:0;top:5022px;width:1200px;text-align:center;font-size:13px;color:var(--muted)}
</style>
</head>
<body>

<header class="hero">
  <svg class="hero-wave" viewBox="0 0 1200 140" preserveAspectRatio="none" aria-hidden="true">
    <path d="M0 100 C 300 150 700 40 1200 70 L1200 140 L0 140 Z" fill="#ffffff"/>
  </svg>
  <div class="abs brand site-brand"><span class="brand-mark"></span>Kovel Digital</div>
  <nav class="abs nav">
    <span>Home</span><span>Services</span><span>Blog</span>
    <span class="nav-social"><span class="dot"></span><span class="dot"></span><span class="dot"></span></span>
  </nav>
  <h1 class="abs">Search Marketing That Actually Delivers</h1>
  <p class="abs hero-lead">Do you want to see an enviable ROI on search marketing? It's possible - you've found us.</p>
  <span class="abs btn hero-btn">Contact Us Today</span>
  <div class="abs hero-art" role="img" aria-label="Illustration of a tablet showing rising bar charts and analytics"></div>
</header>

<div class="abs partners" aria-label="Partner badges">
  <span class="partner"></span><span class="partner"></span><span class="partner"></span>
  <span class="partner"></span><span class="partner"></span><span class="partner"></span>
</div>

<section class="abs intro">
  <h2>We know and understand the world of business</h2>
  <p>We know that <strong>ROI is the single most important metric</strong> in the marketing world. We've worked with some of the world's largest brands, not just in finance, insurance, payday loans and health where achieving above results didn't seem possible. For us, it's just a challenge that can be overcome. Whether you're working with our <a>Pay Per Click Marketing</a>, <a>Organic Search Marketing (SEO)</a>, Email Marketing or <a>Link Building &amp; Outreach</a> – we work with ROI in mind.</p>
  <p><strong>That's why we're known as the ROI driven digital agency.</strong></p>
  <p><strong>Handle your SEO in-house?</strong> Consider using our industry-leading <a>link outreach service</a> to bolster your efforts.</p>
</section>

<section aria-label="Services">
  <div class="abs service" style="left:29px;top:830px">
    <div class="service-icon" role="img" aria-label="Organic search icon"></div>
    <h3>Organic Search</h3>
    <p>Attract traffic that converts and interacts with your brand through Organic. We implement both short-term and long-term campaigns to bolster your success.</p>
  </div>
  <div class="abs service" style="left:435px;top:830px">
    <div class="service-icon" role="img" aria-label="Paid search icon"></div>
    <h3>Paid Search</h3>
    <p>Drive highly converting traffic to your website. Our PPC campaigns are achieved from the start – helping you unlock your business quickly.</p>
  </div>
  <div class="abs service" style="left:845px;top:830px">
    <div class="service-icon" role="img" aria-label="Link outreach icon"></div>
    <h3>Link Outreach</h3>
    <p>The core foundation of any search campaign. Our team of link outreachers are the best in the industry. We secure link placements that drive rankings.</p>
  </div>
  <div class="abs service" style="left:29px;top:1040px">
    <div class="service-icon" role="img" aria-label="UX and CRO icon"></div>
    <h3>UX &amp; CRO</h3>
    <p>Let us dig into your analytic channels and identify where we can bolster your conversion rates with an improving user experience.</p>
  </div>
  <div class="abs service" style="left:435px;top:1040px">
    <div class="service-icon" role="img" aria-label="Email marketing icon"></div>
    <h3>Email Marketing</h3>
    <p>Our targeted email marketing campaigns allow you to segment users and deliver content, tailored campaigns and promotions to different demographics.</p>
  </div>
  <div class="abs service" style="left:845px;top:1040px">
    <div class="service-icon" role="img" aria-label="Social media icon"></div>
    <h3>Social Media</h3>
    <p>Your followers are your most loyal customers. Let us develop a comprehensive strategy that gets your brand seen, building interest and increased sales.</p>
  </div>
</section>

<section aria-label="Growth">
  <svg class="abs growth-band" viewBox="0 0 1200 520" preserveAspectRatio="none" aria-hidden="true">
    <defs>
      <linearGradient id="band" x1="0" y1="0" x2="1" y2="1">
        <stop offset="0" stop-color="#3b8cec"/>
        <stop offset="1" stop-color="#1a5cc9"/>
      </linearGradient>
    </defs>
    <polygon points="0,80 1200,0 1200,470 0,520" fill="url(#band)"/>
  </svg>
  <div class="abs growth-art" role="img" aria-label="Illustration of a desktop monitor showing a dashboard"></div>
  <h2 class="abs growth-title">We grow as our clients grow<br>That's what we love.</h2>
  <div class="abs stat" style="left:44px;top:1730px"><div class="stat-num">117</div><div class="stat-label">Satisfied Clients</div></div>
  <div class="abs stat" style="left:450px;top:1730px"><div class="stat-num">215</div><div class="stat-label">Campaigns Finished</div></div>
  <div class="abs stat" style="left:860px;top:1730px"><div class="stat-num">1798</div><div class="stat-label">Cups of Coffee</div></div>
</section>

<section class="abs seo">
  <h2>Handle SEO Yourself? Perfect.</h2>
  <h4>Hassle-Free Link Placements That Drive Rankings</h4>
  <p>Our link placements are used by some of the world's largest companies in the most difficult industries – such as payday loans, insurance, finance, health and legal. We combine link placement services in conjunction with our <a>Organic Search (SEO)</a> offerings, although some of our clients handle their SEO in-house and prefer to use our link placements to bolster their rankings.</p>
</section>
<div class="abs seo-art" role="img" aria-label="Illustration of a presentation board with bar charts"></div>

<div class="abs process-art" role="img" aria-label="Illustration of a person beside a large web page layout"></div>
<section class="abs process">
  <h2>Here's how our unique,<br>link acquisition process works:</h2>
  <ol>
    <li><b>1.</b> We take your clients URLs and their business sector (or your own sites), and we utilise our connections to try and secure a link placement.</li>
    <li><b>2.</b> All of the sites we outreach to are 100% genuine – we do not own nor control any of the sites.</li>
    <li><b>3.</b> If a webmaster chooses to link to you, it is of their own accord, they have decided to link to you. Thus, you have earned a genuine link.</li>
    <li><b>4.</b> We identify the most relevant page/post on their site, and work with the webmaster to ensure your link fits into their existing content. We write an additional sentence or two to make sure the link fits in with the content.</li>
  </ol>
  <p class="more">Want to learn more and get our pricing? <a>Just click here.</a></p>
</section>

<div class="abs contact-bg"></div>
<div class="abs contact-band"></div>
<div class="abs contact-head">
  <h2>Say Hello!</h2>
  <p>Send us a message using the contact form.<br>Or use information below to reach us.</p>
</div>

<section class="abs card">
  <div class="abs form">
    <h3>We'd Love to Hear from You</h3>
    <div class="field" style="top:60px"><label>Your Name (required)</label><div class="input"></div></div>
    <div class="field" style="top:170px"><label>Your Business Name</label><div class="input"></div></div>
    <div class="field" style="top:280px"><label>Phone</label><div class="input"></div></div>
    <div class="field" style="top:390px"><label>Your Email (required)</label><div class="input"></div></div>
    <div class="field" style="top:500px"><label>Your Message</label><div class="input textarea"></div></div>
    <span class="btn form-btn">Send Message</span>
  </div>
  <div class="abs details">
    <h3>Contact Details</h3>
    <div class="detail" style="top:56px">
      <svg width="16" height="16" viewBox="0 0 16 16" aria-hidden="true"><path d="M8 1a5 5 0 0 0-5 5c0 4 5 9 5 9s5-5 5-9a5 5 0 0 0-5-5zm0 7a2 2 0 1 1 0-4 2 2 0 0 1 0 4z" fill="#2a7fe6"/></svg>
      <span>Kovel Digital Ltd, 14 Harrow Yard,<br>Corbel Lane, Ashfield AF3 2QN</span>
    </div>
    <div class="detail" style="top:120px">
      <svg width="16" height="16" viewBox="0 0 16 16" aria-hidden="true"><path d="M4 1l3 3-2 2a9 9 0 0 0 5 5l2-2 3 3-2 2C7 14 2 9 2 3z" fill="#2a7fe6"/></svg>
      <span>01632 960 418</span>
    </div>
    <div class="detail" style="top:162px">
      <svg width="16" height="16" viewBox="0 0 16 16" aria-hidden="true"><rect x="1" y="3" width="14" height="10" rx="1" fill="#2a7fe6"/><path d="M1.5 4l6.5 5 6.5-5" stroke="#fff" stroke-width="1.3" fill="none"/></svg>
      <span>hello@koveldigital-studio.net</span>
    </div>
    <p class="detail-text" style="top:214px">We're always available during normal working hours 9AM-5PM, Mon-Fri.</p>
    <p class="detail-text" style="top:298px">Whether you're looking for advice and guidance on a new idea you have, or you want us to put together a marketing campaign for you – we'd be more than happy to help.</p>
    <div class="follow">
      <h3>Follow Us</h3>
      <div class="follow-dots"><span class="dot"></span><span class="dot"></span><span class="dot"></span><span class="dot"></span></div>
    </div>
  </div>
</section>

<footer>
  <div class="abs brand footer-brand"><span class="brand-mark"></span>Kovel Digital</div>
  <div class="abs footer-col" style="left:390px">
    <h4>Our Key Services</h4>
    <ul><li>Link Outreach</li><li>Organic Search (SEO)</li><li>Paid Search (PPC)</li><li>Social Media Marketing</li></ul>
  </div>
  <div class="abs footer-col" style="left:630px">
    <h4>Locations (SEO)</h4>
    <ul><li>Birmingham</li><li>Derby</li><li>London</li><li>Manchester</li><li>Stoke on Trent</li></ul>
  </div>
  <div class="abs footer-col" style="left:900px">
    <h4>Ashfield Office</h4>
    <ul><li>Kovel Digital Ltd, 14 Harrow Yard,</li><li>Corbel Lane, Ashfield,</li><li>AF3 2QN</li></ul>
  </div>
  <div class="abs footer-rule"></div>
  <p class="abs copyright">© 2019 Kovel Digital Limited. All rights reserved.</p>
</footer>

</body>
</html>
```